Land Buying Company Needs Letterhead for Direct Mail Marketing to Land Owners

We are looking for a professional letterhead that we will be including in our direct mail marketing. We will be sending this to land owners who may be interested in selling or purchasing land.

The letterhead needs to be editable. Headers and footers would look nice, but we are open. We would want it to include our address, website, phone, and email info. For right now the address to use for design purposes would the following:

Address: 415 Bramwell Avenue #600
Dallas, TX 75219
Website - www.quillridgeacres.example
Email - info@quillridgeacres.example
Phone - 866-402-ACRE

I have attached our logo zip file that we just had done on Pixel Guild. Let me know what questions you have, and thank you.

```html
<!DOCTYPE html>
<html lang="en">
<head>
<meta charset="utf-8">
<title>Quillridge Acres Letterhead</title>
<link rel="stylesheet" href="https://fonts.googleapis.com/css2?family=Montserrat:wght@700&family=Raleway:wght@400&display=swap">
<style>
  :root {
    --lime: #8dc63f;
    --forest: #3f6b1f;
    --pale: #c8e3a0;
    --ink: #6b6b6b;
    --ring: #d5d5d5;
    --paper: #ffffff;
  }
  html, body {
    margin: 0;
    padding: 0;
    overflow: hidden;
    background: var(--paper);
  }
  .letterhead {
    position: relative;
    width: 851px;
    height: 1200px;
    background: var(--paper);
    overflow: hidden;
  }
  .side-bands {
    position: absolute;
    inset: 0;
    width: 851px;
    height: 1200px;
  }
  .corner-accent {
    position: absolute;
    left: 560px;
    top: 0;
    width: 291px;
    height: 245px;
    background: radial-gradient(ellipse at 70% 40%, var(--lime) 0%, var(--pale) 45%, rgba(255,255,255,0) 75%);
  }
  .brand {
    position: absolute;
    left: 62px;
    top: 108px;
    display: flex;
    align-items: center;
    gap: 16px;
  }
  .brand-dot {
    width: 64px;
    height: 64px;
    border-radius: 50%;
    background: var(--forest);
  }
  .brand-name {
    font-family: "Montserrat", sans-serif;
    font-weight: 700;
    font-size: 34px;
    letter-spacing: 1px;
    color: var(--lime);
    margin: 0;
  }
  .contact {
    position: absolute;
    right: 52px;
    top: 930px;
    margin: 0;
    padding: 0;
    list-style: none;
  }
  .contact-item {
    display: flex;
    align-items: center;
    justify-content: flex-end;
    gap: 14px;
    height: 36px;
    margin-bottom: 22px;
    font-family: "Raleway", sans-serif;
    font-size: 17px;
    color: var(--ink);
    white-space: nowrap;
  }
  .contact-icon {
    width: 34px;
    height: 34px;
    flex: none;
  }
</style>
</head>
<body>
<main class="letterhead">
  <svg class="side-bands" viewBox="0 0 851 1200" aria-hidden="true">
    <polygon points="0,0 50,0 50,330 0,372" fill="var(--lime)"/>
    <polygon points="0,396 50,354 50,384 0,426" fill="var(--forest)"/>
    <polygon points="803,882 851,842 851,1200 803,1200" fill="var(--lime)"/>
    <polygon points="803,858 851,818 851,788 803,828" fill="var(--forest)"/>
  </svg>

  <div class="corner-accent" role="img" aria-label="Decorative green geometric accent in the top corner"></div>

  <header class="brand">
    <span class="brand-dot"></span>
    <p class="brand-name">QUILLRIDGE ACRES</p>
  </header>

  <ul class="contact">
    <li class="contact-item">
      <span>866-402-ACRE</span>
      <svg class="contact-icon" viewBox="0 0 34 34" aria-hidden="true">
        <circle cx="17" cy="17" r="16" fill="#fff" stroke="var(--ring)" stroke-width="1.5"/>
        <path d="M12 10c1-1 2.5-1 3 .5l1 2.5c.3.8 0 1.5-.6 2l-1 .8c.8 1.8 2 3 3.8 3.8l.8-1c.5-.6 1.2-.9 2-.6l2.5 1c1.5.5 1.5 2 .5 3l-1 1c-1 1-3 1-5-.2-3-1.8-5.3-4.1-7-7-1.2-2-1.2-4-.2-5z" fill="var(--ink)"/>
      </svg>
    </li>
    <li class="contact-item">
      <span>415 Bramwell Avenue #600, Dallas, TX 75219</span>
      <svg class="contact-icon" viewBox="0 0 34 34" aria-hidden="true">
        <circle cx="17" cy="17" r="16" fill="#fff" stroke="var(--ring)" stroke-width="1.5"/>
        <path d="M17 8a6 6 0 0 0-6 6c0 4.5 6 12 6 12s6-7.5 6-12a6 6 0 0 0-6-6zm0 8.5a2.5 2.5 0 1 1 0-5 2.5 2.5 0 0 1 0 5z" fill="var(--ink)"/>
      </svg>
    </li>
    <li class="contact-item">
      <span>www.quillridgeacres.example</span>
      <svg class="contact-icon" viewBox="0 0 34 34" aria-hidden="true">
        <circle cx="17" cy="17" r="16" fill="#fff" stroke="var(--ring)" stroke-width="1.5"/>
        <circle cx="17" cy="17" r="8" fill="none" stroke="var(--ink)" stroke-width="1.6"/>
        <ellipse cx="17" cy="17" rx="3.5" ry="8" fill="none" stroke="var(--ink)" stroke-width="1.4"/>
        <line x1="9" y1="17" x2="25" y2="17" stroke="var(--ink)" stroke-width="1.4"/>
      </svg>
    </li>
    <li class="contact-item">
      <span>info@quillridgeacres.example</span>
      <svg class="contact-icon" viewBox="0 0 34 34" aria-hidden="true">
        <circle cx="17" cy="17" r="16" fill="#fff" stroke="var(--ring)" stroke-width="1.5"/>
        <rect x="9" y="11.5" width="16" height="11" rx="1" fill="var(--ink)"/>
        <polyline points="9.5,12.5 17,18 24.5,12.5" fill="none" stroke="#fff" stroke-width="1.4"/>
      </svg>
    </li>
  </ul>
</main>
</body>
</html>
```